Optometrist/Eye Care Clinic Business card with new logo attached

We are a small, independent eye care clinic in Canada. We have recently updated our logo (as attached), and would like a professional, modern and health care oriented business card to highlight our office details and our optometrist. We'd like to incorporate the blue colours as seen on our logo.

Target Market(s)

demographic: age 35-65 male/female equal

Industry/Entity Type

Health Care

Contact Information for Business Card

Name of clinic: "Marrow Bend Eye Care Optometry"

Font styles to use
Sans Serif

Colors
0355a3

Requirements
Must have
• our website: marrowbendeyecare.com
• Dr Lena Quorvik
• Optometrist
• 217-392 E Halvering Ave
• Vancouver BC V6R 3J8
• P: 604-319-2058
• E: info@marrowbendeyecare.com
Nice to have
• front side: logo/name of clinic as seen on logo attached and website
• backside: logo on the left side, and name/title/address/phone/email

```html
<!DOCTYPE html>
<html lang="en">
<head>
<meta charset="utf-8">
<title>Marrow Bend Eye Care Optometry – Business Card</title>
<link href="https://fonts.googleapis.com/css2?family=Roboto:wght@300;400;500;700&display=swap" rel="stylesheet">
<style>
  :root {
    --page-bg: #2a2b2e;
    --navy-deep: #0a3a6b;
    --brand-blue: #0355a3;
    --band-teal: #0d4f7e;
    --band-bright: #0a5cc4;
    --accent-sky: #3fa3e0;
    --ink-white: #ffffff;
    --ink-soft: #e6eef8;
  }
  * { box-sizing: border-box; margin: 0; padding: 0; }
  html, body { width: 1200px; height: 800px; overflow: hidden; }
  body {
    background: var(--page-bg);
    font-family: "Roboto", Arial, sans-serif;
    display: flex;
    flex-direction: column;
    align-items: center;
    justify-content: center;
    gap: 40px;
  }
  .card {
    position: relative;
    width: 595px;
    height: 340px;
    overflow: hidden;
    color: var(--ink-white);
    box-shadow: 0 14px 30px rgba(0,0,0,.45);
  }

  /* Front */
  .card-front {
    background: linear-gradient(90deg, var(--navy-deep) 0%, var(--brand-blue) 100%);
  }
  .front-wordmark {
    position: absolute;
    top: 78px;
    left: 0; right: 0;
    text-align: center;
    font-weight: 300;
    font-size: 24px;
    line-height: 1.35;
    letter-spacing: 4px;
    text-transform: uppercase;
    color: var(--ink-white);
  }
  .front-band {
    position: absolute;
    left: 0; right: 0;
    top: 226px;
    height: 74px;
    background: var(--band-teal);
    opacity: .55;
  }
  .front-tagline {
    position: absolute;
    left: 0; right: 0;
    top: 258px;
    text-align: center;
    font-weight: 700;
    font-size: 13px;
  }
  .front-base {
    position: absolute;
    left: 0; right: 0; bottom: 14px;
    height: 30px;
    background: var(--band-bright);
  }

  /* Back */
  .card-back {
    background: linear-gradient(100deg, var(--navy-deep) 0%, var(--brand-blue) 100%);
    padding: 62px 40px 0 40px;
  }
  .back-wordmark {
    font-weight: 300;
    font-size: 19px;
    letter-spacing: 3px;
    text-transform: uppercase;
    line-height: 1.3;
    width: 230px;
    color: var(--ink-white);
  }
  .doctor-name {
    margin-top: 26px;
    font-weight: 500;
    font-size: 18px;
    text-transform: uppercase;
    color: var(--accent-sky);
  }
  .doctor-title {
    margin-top: 2px;
    font-weight: 700;
    font-size: 13px;
  }
  .contact-list {
    list-style: none;
    margin-top: 14px;
  }
  .contact-item {
    display: flex;
    align-items: center;
    gap: 10px;
    font-size: 13px;
    color: var(--ink-soft);
    margin-bottom: 5px;
  }
  .contact-icon {
    width: 20px; height: 20px;
    flex: none;
  }
</style>
</head>
<body>

  <section class="card card-front" aria-label="Business card front">
    <p class="front-wordmark">Marrow Bend<br>Eye Care<br>Optometry</p>
    <div class="front-band"></div>
    <p class="front-tagline">"Marrow Bend Eye Care Optometry"</p>
    <div class="front-base"></div>
  </section>

  <section class="card card-back" aria-label="Business card back">
    <p class="back-wordmark">Marrow Bend Eye Care Optometry</p>
    <h1 class="doctor-name">Dr Lena Quorvik</h1>
    <p class="doctor-title">Optometrist</p>
    <ul class="contact-list">
      <li class="contact-item">
        <svg class="contact-icon" viewBox="0 0 20 20" aria-hidden="true">
          <circle cx="10" cy="10" r="9" fill="none" stroke="#3fa3e0" stroke-width="1.2"/>
          <path d="M7 5.5 l1.6 0 l.8 2.2 -1 .8 a6 6 0 0 0 3 3 l.8-1 2.2.8 0 1.6 a1 1 0 0 1-1 1 A8 8 0 0 1 6 6.5 a1 1 0 0 1 1-1z" fill="#3fa3e0"/>
        </svg>
        604-319-2058
      </li>
      <li class="contact-item">
        <svg class="contact-icon" viewBox="0 0 20 20" aria-hidden="true">
          <circle cx="10" cy="10" r="9" fill="none" stroke="#3fa3e0" stroke-width="1.2"/>
          <rect x="5.5" y="6.5" width="9" height="7" fill="none" stroke="#3fa3e0" stroke-width="1.2"/>
          <path d="M5.5 6.5 L10 10.5 L14.5 6.5" fill="none" stroke="#3fa3e0" stroke-width="1.2"/>
        </svg>
        info@marrowbendeyecare.com
      </li>
      <li class="contact-item">
        <svg class="contact-icon" viewBox="0 0 20 20" aria-hidden="true">
          <circle cx="10" cy="10" r="9" fill="none" stroke="#3fa3e0" stroke-width="1.2"/>
          <circle cx="10" cy="10" r="4.8" fill="none" stroke="#3fa3e0" stroke-width="1.1"/>
          <ellipse cx="10" cy="10" rx="2" ry="4.8" fill="none" stroke="#3fa3e0" stroke-width="1"/>
          <line x1="5.2" y1="10" x2="14.8" y2="10" stroke="#3fa3e0" stroke-width="1"/>
        </svg>
        marrowbendeyecare.com
      </li>
      <li class="contact-item">
        <svg class="contact-icon" viewBox="0 0 20 20" aria-hidden="true">
          <circle cx="10" cy="10" r="9" fill="none" stroke="#3fa3e0" stroke-width="1.2"/>
          <path d="M10 15 C7 11.5 6.5 10 6.5 8.5 a3.5 3.5 0 0 1 7 0 c0 1.5-.5 3-3.5 6.5z" fill="none" stroke="#3fa3e0" stroke-width="1.2"/>
          <circle cx="10" cy="8.5" r="1.2" fill="#3fa3e0"/>
        </svg>
        217-392 E Halvering Ave Vancouver BC V6R 3J8
      </li>
    </ul>
  </section>

</body>
</html>
```